Letter and Envelope Design For Larchmont Realty

Please design a letter and an envelope incorporating our logo (See Attached). We are also launched a business card contest. Since we want them to match, please feel free to submit a design for both the business card and also the letter design and envelope.

Requirements
Must have
• The envelope, the letter and the business cards must match somehow connecting the designs. We want them to have something that holds them together besides the logo.

```html
<!DOCTYPE html>
<html lang="en">
<head>
<meta charset="utf-8">
<title>Larchmont Realty Stationery</title>
<link rel="stylesheet" href="https://fonts.googleapis.com/css2?family=Josefin+Sans:wght@600&family=Open+Sans:wght@400;600&display=swap">
<style>
  :root {
    --navy: #0a1a8c;
    --navy-deep: #07125a;
    --charcoal: #1e1e1e;
    --graphite: #5a5a5c;
    --paper: #ffffff;
    --backdrop: #ffffff;
    --shadow: rgba(0, 0, 0, 0.45);
  }
  * { margin: 0; padding: 0; box-sizing: border-box; }
  html, body { width: 1200px; height: 881px; overflow: hidden; background: var(--backdrop); }
  .stationery { position: relative; width: 1200px; height: 881px; }
  .sheet { position: absolute; background: var(--paper); box-shadow: 0 4px 14px var(--shadow); overflow: hidden; }
  .sheet svg.artwork { position: absolute; inset: 0; width: 100%; height: 100%; }
  .letterhead { left: 37px; top: 48px; width: 469px; height: 723px; }
  .business-card { left: 487px; top: 84px; width: 685px; height: 326px; }
  .envelope { left: 487px; top: 449px; width: 685px; height: 325px; }

  .brand { position: absolute; display: flex; flex-direction: column; align-items: center; text-align: center; color: var(--navy); font-family: "Josefin Sans", sans-serif; font-weight: 600; }
  .brand-circle { border: 3px solid var(--navy); border-radius: 50%; }
  .brand-name { line-height: 1; letter-spacing: 0.12em; text-transform: uppercase; }

  .letterhead .brand { left: 314px; top: 14px; width: 160px; }
  .letterhead .brand-circle { width: 44px; height: 44px; border-width: 2px; margin-bottom: 10px; }
  .letterhead .brand-name { font-size: 15px; }

  .business-card .brand, .envelope .brand { left: 191px; width: 300px; }
  .business-card .brand { top: 20px; }
  .envelope .brand { top: 115px; }
  .business-card .brand-circle, .envelope .brand-circle { width: 88px; height: 88px; margin-bottom: 12px; }
  .business-card .brand-name, .envelope .brand-name { font-size: 24px; line-height: 1.05; }

  .contact-list { position: absolute; list-style: none; color: var(--paper); font-family: "Open Sans", sans-serif; }
  .contact-list li { display: flex; align-items: center; }
  .contact-list svg { flex: none; fill: none; stroke: var(--paper); stroke-width: 1.6; }
  .business-card .contact-list { left: 12px; top: 226px; font-size: 15px; }
  .business-card .contact-list li { height: 25px; gap: 8px; }
  .business-card .contact-list svg { width: 15px; height: 15px; }
  .letterhead .contact-list { left: 5px; top: 663px; font-size: 7px; font-weight: 600; }
  .letterhead .contact-list li { height: 10px; gap: 4px; }
  .letterhead .contact-list svg { width: 7px; height: 7px; stroke-width: 2; }
</style>
</head>
<body>
<main class="stationery">

  <section class="sheet letterhead" aria-label="Letterhead">
    <svg class="artwork" viewBox="0 0 469 723" preserveAspectRatio="none" aria-hidden="true">
      <defs>
        <linearGradient id="lh-blue" x1="0" x2="1"><stop offset="0" stop-color="var(--navy)"/><stop offset="1" stop-color="var(--navy-deep)"/></linearGradient>
        <linearGradient id="lh-dark" x1="0" x2="1"><stop offset="0" stop-color="var(--graphite)"/><stop offset="1" stop-color="var(--charcoal)"/></linearGradient>
      </defs>
      <rect width="469" height="723" fill="url(#lh-blue)"/>
      <path d="M0 104 Q70 2 469 8 L469 680 Q300 690 0 620 Z" fill="var(--paper)"/>
      <path d="M250 700 Q380 690 469 640 L469 723 L310 723 Z" fill="url(#lh-dark)"/>
      <path d="M250 700 Q380 698 469 705" stroke="var(--paper)" stroke-width="2" fill="none"/>
    </svg>
    <div class="brand">
      <div class="brand-circle"></div>
      <p class="brand-name">Larchmont<br>Realty</p>
    </div>
    <ul class="contact-list">
      <li><svg viewBox="0 0 16 16"><path d="M3 2h3l1 4-2 1a8 8 0 0 0 4 4l1-2 4 1v3a1 1 0 0 1-1 1A12 12 0 0 1 2 3a1 1 0 0 1 1-1z"/></svg>+8730492</li>
      <li><svg viewBox="0 0 16 16"><path d="M8 15s5-5 5-9a5 5 0 0 0-10 0c0 4 5 9 5 9z"/><circle cx="8" cy="6" r="2"/></svg>Elm Crest Road 48. NC</li>
      <li><svg viewBox="0 0 16 16"><circle cx="8" cy="8" r="6.5"/><path d="M1.5 8h13M8 1.5c3 3.5 3 9.5 0 13M8 1.5c-3 3.5-3 9.5 0 13"/></svg>larchmontrealty.com</li>
      <li><svg viewBox="0 0 16 16"><rect x="1.5" y="3.5" width="13" height="9"/><path d="M1.5 3.5 8 9l6.5-5.5"/></svg>lmr_realty.com</li>
    </ul>
  </section>

  <section class="sheet business-card" aria-label="Business card">
    <svg class="artwork" viewBox="0 0 685 326" preserveAspectRatio="none" aria-hidden="true">
      <defs>
        <linearGradient id="bc-blue" x1="0" x2="1"><stop offset="0" stop-color="var(--navy)"/><stop offset="1" stop-color="var(--navy-deep)"/></linearGradient>
        <linearGradient id="bc-dark" x1="0" x2="1"><stop offset="0" stop-color="var(--graphite)"/><stop offset="1" stop-color="var(--charcoal)"/></linearGradient>
      </defs>
      <path d="M0 153 C60 215 250 275 685 300 L685 326 L0 326 Z" fill="url(#bc-blue)"/>
      <path d="M387 277 Q560 262 685 195 L685 297 Q540 288 387 277 Z" fill="url(#bc-dark)"/>
      <path d="M387 279 Q560 291 685 299" stroke="var(--paper)" stroke-width="2.5" fill="none"/>
    </svg>
    <div class="brand">
      <div class="brand-circle"></div>
      <p class="brand-name">Larchmont<br>Realty</p>
    </div>
    <ul class="contact-list">
      <li><svg viewBox="0 0 16 16"><path d="M3 2h3l1 4-2 1a8 8 0 0 0 4 4l1-2 4 1v3a1 1 0 0 1-1 1A12 12 0 0 1 2 3a1 1 0 0 1 1-1z"/></svg>+8730492</li>
      <li><svg viewBox="0 0 16 16"><path d="M8 15s5-5 5-9a5 5 0 0 0-10 0c0 4 5 9 5 9z"/><circle cx="8" cy="6" r="2"/></svg>Elm Crest Road 48. NC</li>
      <li><svg viewBox="0 0 16 16"><circle cx="8" cy="8" r="6.5"/><path d="M1.5 8h13M8 1.5c3 3.5 3 9.5 0 13M8 1.5c-3 3.5-3 9.5 0 13"/></svg>larchmontrealty.com</li>
      <li><svg viewBox="0 0 16 16"><rect x="1.5" y="3.5" width="13" height="9"/><path d="M1.5 3.5 8 9l6.5-5.5"/></svg>lmr_realty.com</li>
    </ul>
  </section>

  <section class="sheet envelope" aria-label="Envelope">
    <svg class="artwork" viewBox="0 0 685 325" preserveAspectRatio="none" aria-hidden="true">
      <defs>
        <linearGradient id="env-blue" x1="0" x2="1"><stop offset="0" stop-color="var(--navy)"/><stop offset="1" stop-color="var(--navy-deep)"/></linearGradient>
        <linearGradient id="env-dark" x1="0" x2="1"><stop offset="0" stop-color="var(--graphite)"/><stop offset="1" stop-color="var(--charcoal)"/></linearGradient>
      </defs>
      <path d="M0 0 H685 L643 95 H45 Z" fill="url(#env-blue)"/>
      <rect y="283" width="685" height="42" fill="url(#env-dark)"/>
    </svg>
    <div class="brand">
      <div class="brand-circle"></div>
      <p class="brand-name">Larchmont<br>Realty</p>
    </div>
  </section>

</main>
</body>
</html>
```